Template for a Holiday Look Book

We need a holiday lookbook that we can use at a few different golf and country clubs. I am hoping we can get a design nailed down, that they would then be able to tweak and alter from club to club. We have Marketing Directors at each Club, but no one has the time to make this from scratch, but could tweak it much easier once the template is created. I have attached a word document with ideas and have a google file we have started for pictures as well.

Target Market(s)

counrty club members

Industry/Entity Type

Country Club

Font styles to use
Sans Serif

Colors
0355a3
ffffff
eaf1f7

Requirements
Must have
• holiday look and feel....enticing the items that would be purchased

```html
<!DOCTYPE html>
<html lang="en">
<head>
<meta charset="utf-8">
<title>Holiday Lookbook Cover</title>
<link rel="stylesheet" href="https://fonts.googleapis.com/css2?family=Raleway:wght@300;400;500&display=swap">
<style>
  :root {
    --club-blue: #0355a3;
    --white: #ffffff;
    --ice: #eaf1f7;
    --stage: #e4e6e8;
    --ink: #3b3f44;
    --teal: #3ab3c4;
    --turf-dark: #2c4a22;
    --turf-mid: #5d7f3a;
    --turf-light: #a9b98a;
  }
  * { margin: 0; padding: 0; box-sizing: border-box; }
  html, body {
    width: 1200px; height: 901px; overflow: hidden;
    background: var(--stage);
    font-family: "Raleway", sans-serif;
  }
  .cover {
    position: absolute; left: 80px; top: 90px;
    width: 1040px; height: 720px;
    background: var(--white);
    overflow: hidden;
    box-shadow: 0 10px 30px rgba(0,0,0,0.12);
  }
  .cover-art { position: absolute; inset: 0; }
  .edition {
    position: absolute; left: 44px; top: 80px;
    color: var(--ink);
  }
  .edition-title {
    font-size: 24px; font-weight: 300; letter-spacing: 1px;
  }
  .edition-years {
    display: flex; align-items: center; gap: 10px;
    margin-top: 6px; font-size: 15px; font-weight: 300; letter-spacing: 1px;
    color: var(--club-blue);
  }
  .edition-years svg { width: 10px; height: 12px; }
  .tagline {
    position: absolute; left: 112px; top: 540px;
    color: var(--white);
    font-size: 25px; font-weight: 300; line-height: 1.3; letter-spacing: 0.5px;
    text-transform: uppercase;
  }
  .web-address {
    position: absolute; left: 112px; top: 640px;
    color: var(--white);
    font-size: 12px; font-weight: 400; letter-spacing: 0.5px;
    opacity: 0.85;
  }
  .club-name {
    position: absolute; left: 790px; top: 330px; width: 220px;
    display: flex; flex-direction: column; align-items: center; gap: 14px;
    color: var(--club-blue);
    font-size: 24px; font-weight: 500; line-height: 1.2; text-align: center;
  }
  .club-mark {
    width: 34px; height: 34px; background: var(--club-blue);
  }
</style>
</head>
<body>
  <main class="cover">
    <svg class="cover-art" viewBox="0 0 1040 720" width="1040" height="720">
      <defs>
        <linearGradient id="turf" x1="0" y1="0" x2="0" y2="1">
          <stop offset="0" stop-color="#c9cfc4"/>
          <stop offset="0.3" stop-color="var(--turf-light)"/>
          <stop offset="0.55" stop-color="var(--turf-mid)"/>
          <stop offset="1" stop-color="var(--turf-dark)"/>
        </linearGradient>
      </defs>
      <polygon class="hero-photo" role="img"
        aria-label="Photo of a golf ball on a tee beside a driver head on the green"
        points="280,0 790,0 610,720 60,720" fill="url(#turf)"/>
      <polygon class="light-strip" points="560,0 650,0 470,720 380,720" fill="var(--white)" opacity="0.18"/>
      <polygon class="teal-facet" points="330,300 600,300 520,620 330,620" fill="var(--teal)" opacity="0.55"/>
      <polygon class="shade-facet" points="160,330 440,330 340,720 60,720" fill="var(--turf-dark)" opacity="0.45"/>
      <rect class="accent-block" x="0" y="320" width="120" height="140" fill="var(--club-blue)"/>
      <polygon class="white-slash" points="790,0 1040,0 1040,720 610,720" fill="var(--white)"/>
    </svg>

    <header class="edition">
      <h1 class="edition-title">HOLIDAY LOOKBOOK</h1>
      <p class="edition-years">
        <svg viewBox="0 0 10 12"><polygon points="0,0 10,6 0,12" fill="#0355a3"/></svg>
        2019-2020
      </p>
    </header>

    <p class="tagline">Lifestyle of privacy,<br>luxury, and relaxation</p>
    <p class="web-address">www.ashfordridgecountryclub.com</p>

    <div class="club-name">
      <span class="club-mark"></span>
      <span>Ashford Ridge<br>Country Club</span>
    </div>
  </main>
</body>
</html>
```